Business card design for upmarket Home Technology design and Installation company

Hello designers, we need a great business card designed.
We need it to convey high tech, and also sophistication .
We work with some of the most affluent people in the world building them home technology systems, and A/V entertainment systems.

Services offered include the following:
Design, sales, installation, and maintenance of

*Home Automation systems
*Distributed / Multi-Room Audio and Video
*High Performance Networks & WiFi
* Lighting and Shade Control
*Home cinema
*Security and CCTV Systems

I have included a copy of our logo to use for your design efforts.

Target Market(s)

Upmarket clients with multi million euro villas.

Industry/Entity Type

Home technology

Contact Information for Business Card

NAME: Derek Halloran ADDRESS: Plaza Brisa Local 42, Port Solmera, 07392 PHONE: +34-602-518-794 EMAIL: DHalloran@VELTRAsmarthomes.com WEB: www.veltrasmarthomes.com

Requirements
Must have
• Our Logo, and our tagline

```html
<!DOCTYPE html>
<html lang="en">
<head>
<meta charset="utf-8">
<title>VELTRA Smart Homes – Business Card</title>
<link rel="stylesheet" href="https://fonts.googleapis.com/css2?family=Montserrat:wght@300;400;600;700&display=swap">
<style>
  :root {
    --backdrop: #e4e4e4;
    --card-black: #0a0a0a;
    --gold: #c9a45c;
    --text-white: #f2f2f2;
  }
  * { box-sizing: border-box; margin: 0; padding: 0; }
  html, body {
    width: 1200px; height: 813px; overflow: hidden;
    background: var(--backdrop);
    font-family: "Montserrat", Arial, sans-serif;
  }
  .stage { position: relative; width: 1200px; height: 813px; }
  .card {
    position: absolute; top: 252px;
    width: 540px; height: 309px;
    background: var(--card-black);
    color: var(--text-white);
  }
  .card-back { left: 40px; }
  .card-front { left: 620px; }

  .wordmark {
    position: absolute;
    display: flex; align-items: center; gap: 10px;
    font-weight: 300; color: var(--gold);
    letter-spacing: 0.18em;
  }
  .wordmark-dot {
    width: 12px; height: 12px; border-radius: 50%;
    background: var(--gold);
  }
  .card-back .wordmark { left: 30px; top: 48px; font-size: 36px; }
  .card-front .wordmark { right: 32px; top: 48px; font-size: 34px; }

  .services { position: absolute; left: 30px; top: 112px; }
  .services-heading { color: var(--gold); font-weight: 700; font-size: 15px; margin-bottom: 7px; }
  .services-intro { font-size: 12.5px; margin-bottom: 6px; }
  .services-list { list-style: none; }
  .services-list li {
    display: flex; align-items: center; gap: 10px;
    font-size: 12.5px; line-height: 20px;
  }
  .bullet {
    width: 9px; height: 9px; border-radius: 50%;
    border: 1.6px solid var(--gold); flex: none;
  }

  .identity { position: absolute; left: 30px; top: 136px; display: flex; gap: 10px; }
  .identity-bar { width: 7px; height: 38px; background: var(--gold); margin-top: 14px; }
  .person-name { color: var(--gold); font-weight: 700; font-size: 17px; text-transform: uppercase; }
  .person-role { font-size: 12px; margin-top: 2px; }

  .address { position: absolute; left: 47px; top: 198px; font-size: 12.5px; line-height: 18px; }
  .contacts { position: absolute; left: 47px; top: 242px; list-style: none; }
  .contacts li { display: flex; align-items: center; gap: 7px; font-size: 12.5px; line-height: 18px; }
  .contacts svg { width: 11px; height: 11px; fill: var(--gold); flex: none; }
</style>
</head>
<body>
<main class="stage">

  <section class="card card-back" aria-label="Card back">
    <div class="wordmark"><span class="wordmark-dot"></span>VELTRA</div>
    <div class="services">
      <h2 class="services-heading">Services offered include the following:</h2>
      <p class="services-intro">Design, sales, installation, and maintenance of</p>
      <ul class="services-list">
        <li><span class="bullet"></span>Home Automation systems</li>
        <li><span class="bullet"></span>Distributed / Multi-Room Audio and Video</li>
        <li><span class="bullet"></span>High Performance Networks &amp; WiFi</li>
        <li><span class="bullet"></span>Lighting and Shade Control</li>
        <li><span class="bullet"></span>Home cinema</li>
        <li><span class="bullet"></span>Security and CCTV Systems</li>
      </ul>
    </div>
  </section>

  <section class="card card-front" aria-label="Card front">
    <div class="wordmark">VELTRA</div>
    <div class="identity">
      <span class="identity-bar"></span>
      <div>
        <h1 class="person-name">Derek Halloran</h1>
        <p class="person-role">Founder</p>
      </div>
    </div>
    <p class="address">Plaza Brisa Local 42,<br>Port Solmera, 07392</p>
    <ul class="contacts">
      <li>
        <svg viewBox="0 0 24 24" aria-hidden="true"><path d="M6.6 10.8a15.1 15.1 0 0 0 6.6 6.6l2.2-2.2a1 1 0 0 1 1-.25 11.4 11.4 0 0 0 3.6.57 1 1 0 0 1 1 1V20a1 1 0 0 1-1 1A17 17 0 0 1 3 4a1 1 0 0 1 1-1h3.5a1 1 0 0 1 1 1c0 1.25.2 2.45.57 3.57a1 1 0 0 1-.25 1z"/></svg>
        +34-602-518-794
      </li>
      <li>
        <svg viewBox="0 0 24 24" aria-hidden="true"><path d="M2 5h20v14H2zm2 2v.5l8 5 8-5V7l-8 5z"/></svg>
        DHalloran@VELTRAsmarthomes.com
      </li>
      <li>
        <svg viewBox="0 0 24 24" aria-hidden="true"><path d="M12 2a10 10 0 1 0 0 20 10 10 0 0 0 0-20zm0 2c.9 1.2 1.6 2.6 2 4h-4c.4-1.4 1.1-2.8 2-4zM4.3 14a8 8 0 0 1 0-4h3.4a16 16 0 0 0 0 4zm.9 2h3c.3 1.3.8 2.5 1.4 3.6A8 8 0 0 1 5.2 16zm3-8h-3a8 8 0 0 1 4.4-3.6C8.9 5.5 8.5 6.7 8.2 8zM12 20c-.9-1.2-1.6-2.6-2-4h4c-.4 1.4-1.1 2.8-2 4zm2.3-6H9.7a14 14 0 0 1 0-4h4.6a14 14 0 0 1 0 4zm.1 5.6c.6-1.1 1.1-2.3 1.4-3.6h3a8 8 0 0 1-4.4 3.6zm1.9-5.6a16 16 0 0 0 0-4h3.4a8 8 0 0 1 0 4zm-.5-6c-.3-1.3-.8-2.5-1.4-3.6A8 8 0 0 1 18.8 8z"/></svg>
        www.veltrasmarthomes.com
      </li>
    </ul>
  </section>

</main>
</body>
</html>
```